*** Business Card Design Project

I need a logo and business card for my new catering business: "Pomelia". The design should be modern, clean, elegant and refined. One or Two colours only. The design SHOULD NOT include graphics or images. There should be space for my name, phone number and email address (I will provide these to you later).

Industry/Entity Type

Catering

Requirements
Must have
• Must have one or two colours only.
Must include the text "pomelia"
Should not have
• Must not have graphics or images.

```html
<!DOCTYPE html>
<html lang="en">
<head>
<meta charset="utf-8">
<title>Pomelia – Business Card</title>
<link rel="stylesheet" href="https://fonts.googleapis.com/css2?family=Cinzel:wght@400;600&display=swap">
<style>
  :root {
    --page-bg: #ece7df;
    --card-white: #ffffff;
    --brand-brown: #7a5f42;
    --motto-brown: #5b4630;
    --rule-grey: #b9bcc4;
    --rule-light: #dfe1e6;
    --text-light: #f4efe8;
  }
  * { margin: 0; padding: 0; box-sizing: border-box; }
  html, body {
    width: 1200px;
    height: 1029px;
    overflow: hidden;
    background: var(--page-bg);
  }
  .canvas {
    position: relative;
    width: 1200px;
    height: 1029px;
  }
  .card {
    position: absolute;
    left: 124px;
    top: 210px;
    width: 952px;
    height: 583px;
    background: var(--card-white);
    box-shadow: 6px 8px 14px rgba(0, 0, 0, 0.28);
    overflow: hidden;
    font-family: "Cinzel", serif;
  }
  .band-top {
    position: absolute;
    left: 0; top: 0;
    width: 100%; height: 42px;
    background: var(--brand-brown);
  }
  .rule-top {
    position: absolute;
    left: 0; top: 46px;
    width: 100%; height: 4px;
    background: linear-gradient(var(--rule-light), var(--rule-grey));
  }
  .rule-bottom {
    position: absolute;
    left: 0; top: 498px;
    width: 100%; height: 10px;
    border-top: 3px solid var(--rule-grey);
    border-bottom: 3px solid var(--rule-light);
  }
  .band-bottom {
    position: absolute;
    left: 0; top: 514px;
    width: 100%; height: 69px;
    background: var(--brand-brown);
  }
  .brand {
    position: absolute;
    left: 0;
    top: 268px;
    width: 466px;
    text-align: center;
    color: var(--brand-brown);
  }
  .brand-name {
    font-size: 64px;
    font-weight: 400;
    letter-spacing: 6px;
    line-height: 1;
  }
  .brand-motto {
    font-size: 23px;
    font-weight: 400;
    line-height: 31px;
    color: var(--motto-brown);
  }
  .contact-panel {
    position: absolute;
    left: 497px;
    top: 140px;
    width: 470px;
    height: 286px;
    background: var(--brand-brown);
    border-radius: 14px 0 0 14px;
    box-shadow: 0 3px 8px rgba(0, 0, 0, 0.35);
    color: var(--text-light);
    padding: 84px 0 0 77px;
  }
  .contact-name {
    font-size: 42px;
    font-weight: 400;
    line-height: 1;
    letter-spacing: 1px;
  }
  .contact-line {
    font-size: 24px;
    line-height: 33px;
  }
  .contact-name + .contact-line { margin-top: 8px; }
</style>
</head>
<body>
  <div class="canvas">
    <div class="card">
      <div class="band-top"></div>
      <div class="rule-top"></div>

      <div class="brand">
        <div class="brand-name">POMELIA</div>
        <div class="brand-motto">BUSINESS ADDRESS OR MOTTO<br>CAN BE PLACED HERE</div>
      </div>

      <div class="contact-panel">
        <div class="contact-name">Clara Moss</div>
        <div class="contact-line">(555) 555-0192</div>
        <div class="contact-line">MOSS@EMAIL.COM</div>
      </div>

      <div class="rule-bottom"></div>
      <div class="band-bottom"></div>
    </div>
  </div>
</body>
</html>
```